依頼概要
■依頼の目的/概要
弊社が販売している牛脂のラベルデザインをお願いします。

■依頼詳細
高級感 プレミアム感 上質感 を感じる品のあるデザイン希望です

■その他要望
素人考えだと黒とか金とか、焦げ茶しか浮かびませんがほかに提案があればぜひ

その他何かご不明な点がございましたら、お気軽にご質問下さい。
よろしくお願いいたします。
肉牛は9割がオスなんだそうです、でも本当はメスのほうが脂肪が付きやすく肉質がきめ細かく柔らかいのでおいしいそうです。不飽和脂肪酸もメスのほうが多く、融点が低いので、とろけるような味わいとなります。だからオスは、かわいそうですが小さい時に去勢されてしなうのですって。そうすることでメス肉のおいしい肉質に近づき、あまり変わらない感じになるのだそうです。ちなみに、オスのほうが体が大きいので出荷するときの1頭あたりの価格は「高い」んだそうですよ。みなさん・・・藤波牛は全部メスっていうの、知ってました?しかもバージンのメス、しかも若いメスにこだわって出荷しているとのことです。若くてバージンのメスのほうがやっぱりおいしいのでしょうか(なんかちょっとショックです)でも当たり前ですが、オスより安いからと言って若くてバージンのメスばかり食べていたら牛の数が減りますからね。なるほど、肉牛の9割はオスというのは、納得ですね。

美味しい牛かどうかは最終的には「見た目」で判断されるそうで、購入する人はどこを見ているかというと、肩、腰、お尻などを見るそうです。

等級は、①保留等級 ②肉質等級 ③脂肪交雑 などの基準で格付けや等級が決められていて、上に来ているほうがより評価が高いと判断されます。Aー5-12等級が一番いいお肉ということになりますね。でも、等級が高いからと言ってうまい肉だとは限らないそうで、おいしい餌を見極めるためには①エサ ②生育環境 ③取引実績 などから総合的に判断しないといけなくて、そこが「プロの仕事」なんだというわけですね。

梶山牛の特徴は、何といっても「熟成期間」と「生育環境」にあるそうです。普通子牛は、
6か月になったらセリに出荷されます。それから肥育農家で育てられ、普通26か月で
出荷されるところ、梶山牛は30か月以上で出荷されるので、熟成されてより味が深くなるそうです。餌なのですが、一般的な肥育農家さんでは配合肥料を与えていて、防腐剤や抗生剤、成長ホルモン様物質が入っていて、1か月おいていても腐らないのだそうです。梶山牛は配合飼料を使わず、生産者の梶山典久さんが厳選した餌を2日に1度、自分
でブレンドして与えていて、配合されるので通常より手間も費用もとてもかかっていています(配合は秘密だそうです)自分で素材を吟味し、保存料や、化学物質などのリスクを避けています。
ストレスの少ない環境でのびのび育った梶山牛は、安全性と肉の美味しさ、柔らかさが世界的にも高く評価されていて、プロがうなる高級食材です。月に30頭しか出荷されず、そのうち10頭はヨーロッパに出荷されるので国内では20頭しか流通していません。そのため大変貴重で「幻の梶山牛」と呼ばれています。

〈牛脂について〉
この牛脂は、製造してくださる古典フレンチのレストラン、ロワゾンテのオーナーシェフが普段お店で出している、Aー5-10、11等級の梶山牛の「ケンネ」という胸のあたりにある脂肪の多い部分を使っています。シェフの柚木さんは、生産者の梶山さ
んと古くから付き合いがあり、メス、バージンの梶山牛を特に選んでおろしてもらっているそうです。ということは、この牛脂はAー5-10~11等級、しかもメスでバージンの牛脂なのですがその貴重さが・・・このくどくどした説明でわかっていただけたら嬉しいです!! しかも完全無添加です。

肉の美味しさを一番知っているのは、誰だと思いますか?私は、毎日お客さんに代金を支払ってお客さんに食べさせることを繰り返しているプロの料理人だと思います。

今回の牛脂を作ってくださった料理人の柚木さんを紹介します。肉もピンからキリ、牛脂もピンからキリだそうですが、料理人が選び抜いた、本物の梶山牛の最上級牛脂は「さすが」のうまさで、安い肉でもこの牛脂で焼くと高級な深みが出ます。

現在、梶山牛の牛脂は一般流通しておらず、柚木さんの料理人としての「眼」と「腕」のことを知っている全国のプロの料理人に、個人的にしか牛脂を分けてあげていなかったということですので、製品化させてもらえて・・・本当によかったなぁと思います。

食肉を扱うには、食肉加工の特別な免許や、厳しい衛生基準、施設要件があり、食肉加工の免許を持っている料理人は全国でもほとんどいないそうです。全国調理匠連盟に所属され、宮崎の食材を使った商品開発のアドバイザー、相談役としても活躍されていらっしゃいます。

食品加工の際の衛生面・安全面でも、安心していただいていいです。
<今後の販売について>
梶山牛は前述のとおり希少価値の非常に高い牛で、と殺した時しか牛脂が出ませんので、今後も数量限定の販売になります。タイミングがあるため、ご注文いただいてから実際にお届けできるまで時間をいただくことがあります。予めご了承ください。

```html
<!DOCTYPE html>
<html lang="ja">
<head>
<meta charset="utf-8">
<title>幻の梶山牛 牛脂 ラベル</title>
<link rel="stylesheet" href="https://fonts.googleapis.com/css2?family=Yuji+Boku&family=Shippori+Mincho:wght@600&display=swap">
<style>
  :root {
    --page: #f3f1ec;
    --navy: #1c2160;
    --navy-deep: #12163f;
    --gold-light: #f6e3a1;
    --gold: #d2a64a;
    --gold-dark: #8a6420;
  }
  * { margin: 0; padding: 0; box-sizing: border-box; }
  html, body {
    width: 714px; height: 1200px; overflow: hidden;
    background: var(--page);
  }
  .canvas { position: relative; width: 714px; height: 1200px; }

  .label {
    position: absolute; left: 57px; top: 300px;
    width: 600px; height: 600px;
    background: radial-gradient(circle at 50% 40%, var(--navy) 0%, var(--navy-deep) 100%);
    box-shadow: 0 4px 14px rgba(0,0,0,.18);
  }
  .label__frame {
    position: absolute; inset: 16px;
    border: 5px solid var(--gold);
    outline: 2px solid var(--gold-dark);
    outline-offset: 5px;
  }
  .label__frame::after {
    content: ""; position: absolute; inset: 8px;
    border: 1.5px solid var(--gold);
  }

  .gold {
    font-family: "Yuji Boku", serif;
    background: linear-gradient(180deg, var(--gold-light) 0%, var(--gold) 55%, var(--gold-dark) 100%);
    -webkit-background-clip: text; background-clip: text;
    color: transparent;
  }
  .vertical { position: absolute; writing-mode: vertical-rl; line-height: 1; }

  .origin { right: 62px; top: 52px; font-size: 74px; }
  .brand-name { right: 150px; top: 74px; font-size: 72px; }
  .notice {
    left: 140px; top: 100px; font-size: 26px; letter-spacing: 2px;
    font-family: "Shippori Mincho", serif; font-weight: 600;
  }
  .product {
    position: absolute; left: 250px; top: 438px;
    font-size: 132px; line-height: 1; letter-spacing: 4px;
  }
  .cow-mark {
    position: absolute; left: 110px; top: 466px;
    width: 130px; height: 80px;
    background: linear-gradient(180deg, var(--gold-light), var(--gold));
    border-radius: 6px;
  }
</style>
</head>
<body>
<main class="canvas">
  <section class="label">
    <div class="label__frame"></div>
    <p class="vertical gold origin">宮崎県産</p>
    <p class="vertical gold brand-name">幻の梶山牛</p>
    <p class="vertical gold notice">数量限定販売・完全無添加</p>
    <div class="cow-mark" role="img" aria-label="金色の牛のシルエット"></div>
    <p class="gold product">牛脂</p>
  </section>
</main>
</body>
</html>
```